Design a CD Cover For Baby Music and Lullabies To Appear on Tune Harbor Shop etc.

Please read this brief before you design. Otherwise you will be wasting your time.

I need a cd cover for music albums which will appear on streaming sites such as Tune Harbor Shop Wavelane, Pluvix etc. for the brand Cozy Cradle Tunes. The thumbnails are quite small so the text needs to be quite large.

I need a design if possible, in which I can simply alter the title of the album and the baby picture so that each album has a different cover but works with the branding.

You can check out the Cozy Cradle Tunes on the Tune Harbor shop.
https://play.wavelane.example/artist/7qk3RtLmWvNx82hYbPdaZe

I made those covers and I really don't like them at all! As you can tell I am not a graphic designer. Ha.

Please help me with a modern, eye catching and cute design that will work across the brand now and in the future. The CCT logo and the name Cozy Cradle Tunes is the only thing that needs to be used somewhere in the design.

Please use the title

Soft Hush Tones For Nap Time Part First

for this first album.
(White noise sounds are hair dryers, vacuum cleaners, fans, wind, rain, the sea, white noise, pink noise, brown noise etc. )

Here is an example of album covers which are coherent. A style like this without the over the top text would be good. But don't copy these!
https://play.wavelane.example/artist/9TfKxcMnEuGh31oAsQbiR5

Target Market(s)

Parents of babies.

Font styles to use
Serif
Sans Serif

Colors

Designer to choose colors to be used in the design.

Requirements
Must have
• Large font so it can been seen in the wavelane thumbnail. A photo of a baby. Please take a look at the wavelane and tune harbor stores. The Cozy Cradle Tunes logo.
• Album Title
• Soft Hush Tones For Nap Time Part First

```html
<!DOCTYPE html>
<html lang="en">
<head>
<meta charset="utf-8">
<title>Soft Hush Tones For Nap Time Part First — Album Cover</title>
<link rel="stylesheet" href="https://fonts.googleapis.com/css2?family=Cinzel+Decorative:wght@700&display=swap">
<style>
  :root {
    --page-bg: #ffffff;
    --sky-blue: #4574b4;
    --deep-cloud: #2c62ab;
    --pale-cloud: #cfe8f6;
    --cloud-white: #ffffff;
    --title-yellow: #ffef1f;
    --moon-yellow: #f6d94a;
    --cap-pink: #f07ab2;
    --skin-warm: #e9c2ab;
    --blanket-cream: #e9dccb;
    --stripe-grey: #8d8f95;
  }
  html, body {
    margin: 0;
    padding: 0;
    width: 1200px;
    height: 711px;
    overflow: hidden;
    background: var(--page-bg);
  }
  .stage {
    position: relative;
    width: 1200px;
    height: 711px;
    display: flex;
    align-items: center;
    justify-content: center;
  }
  .album-cover {
    width: 640px;
    height: 640px;
    display: block;
  }
  .album-title {
    font-family: "Cinzel Decorative", Georgia, serif;
    font-weight: 700;
    fill: var(--title-yellow);
  }
  .album-title--main { font-size: 38px; }
  .album-title--part { font-size: 28px; }
  .brand-name {
    font-family: "Cinzel Decorative", Georgia, serif;
    font-weight: 700;
    font-size: 15px;
    fill: var(--title-yellow);
  }
</style>
</head>
<body>
<main class="stage">
  <svg class="album-cover" viewBox="0 0 640 640" xmlns="http://www.w3.org/2000/svg" aria-labelledby="cover-title">
    <title id="cover-title">Cozy Cradle Tunes — Soft Hush Tones For Nap Time, Part First</title>
    <defs>
      <path id="title-arc" d="M 40 300 A 281.8 281.8 0 0 1 600 300"/>
      <linearGradient id="moon-fill" x1="0" y1="0" x2="0" y2="1">
        <stop offset="0" stop-color="var(--cap-pink)"/>
        <stop offset="0.45" stop-color="var(--moon-yellow)"/>
        <stop offset="1" stop-color="#8fc8ec"/>
      </linearGradient>
      <linearGradient id="photo-fill" x1="0" y1="0" x2="1" y2="1">
        <stop offset="0" stop-color="var(--skin-warm)"/>
        <stop offset="0.6" stop-color="#f1d4c2"/>
        <stop offset="1" stop-color="var(--blanket-cream)"/>
      </linearGradient>
      <clipPath id="cover-clip"><rect width="640" height="640"/></clipPath>
    </defs>

    <g clip-path="url(#cover-clip)">
      <rect class="sky" width="640" height="640" fill="var(--sky-blue)"/>

      <path class="cloud-band cloud-band--deep"
        d="M0 360 Q40 330 90 345 Q140 300 200 330 Q250 300 300 335 Q350 310 400 330 Q460 290 520 310 Q560 250 610 230 Q630 180 640 160 L640 640 L0 640 Z"
        fill="var(--deep-cloud)"/>

      <path class="cloud-band cloud-band--pale"
        d="M0 430 Q40 400 90 425 Q130 385 190 410 Q240 370 300 395 Q350 365 400 380 Q440 330 500 345 Q530 300 580 310 Q610 280 640 300 L640 640 L0 640 Z"
        fill="var(--pale-cloud)"/>

      <path class="cloud-band cloud-band--white"
        d="M0 470 Q40 450 80 470 Q120 430 170 450 Q210 415 260 425 Q300 395 350 405 Q400 370 450 380 Q500 345 550 355 Q590 320 640 335 L640 640 L0 640 Z"
        fill="var(--cloud-white)"/>

      <g class="baby-photo" role="img" aria-label="Photo of a sleeping newborn baby in a striped outfit resting on a soft cream blanket">
        <path d="M250 640 L250 470 Q270 410 340 405 Q380 370 440 380 Q490 345 545 355 Q590 320 640 335 L640 640 Z"
          fill="url(#photo-fill)"/>
        <path d="M560 335 Q600 320 640 335 L640 560 Q600 520 560 470 Z" fill="var(--stripe-grey)" opacity="0.55"/>
      </g>

      <g class="moon-illustration" role="img" aria-label="Illustration of a baby in a night cap sleeping on a crescent moon among stars and clouds">
        <rect x="250" y="90" width="115" height="115" rx="38" fill="url(#moon-fill)"/>
      </g>

      <text class="brand-name" x="307" y="234" text-anchor="middle">Cozy Cradle Tunes</text>

      <text class="album-title album-title--main" text-anchor="middle">
        <textPath href="#title-arc" startOffset="50%" textLength="770" lengthAdjust="spacingAndGlyphs">Soft Hush Tones For Nap Time</textPath>
      </text>
      <text class="album-title album-title--part" x="470" y="300" text-anchor="middle">Part First</text>
    </g>
  </svg>
</main>
</body>
</html>
```